Brightstep Foot Care Advertisement Sandwich board

We need a Sandwich board design for our fungal nail clinic - please find attached the sandwich board dimensions.

The sandwich board itself will be displayed outside of a large health clinic and we need it to attract the attention of people walking by. We need a brochure holder included in the design which will hold our brochures which provides as clients with more information (please see attached also).

We are open to the designers creativity but we would like a similar theme portrayed on our board that is similar to our website (www.brightstepfootcare.co.nz) and brochure that incorporates our logo which I have attached). The final design should communicate professionalism and be a minimalist look but modern to capture the attention of pedestrians.

Finally, we would like the website and phone number (07) 312 5840.

We look forward to seeing your work.

```html
<!DOCTYPE html>
<html lang="en">
<head>
<meta charset="utf-8">
<title>Brightstep Foot Care – Sandwich Board</title>
<link rel="stylesheet" href="https://fonts.googleapis.com/css2?family=Bebas+Neue&family=Cinzel:wght@600&family=Open+Sans:wght@700;800&display=swap">
<style>
  :root {
    --canvas-bg: #1a1a1a;
    --board-white: #ffffff;
    --brand-blue: #4b80f0;
    --deep-blue: #1f3f8f;
    --accent-cyan: #7ff0f5;
    --skin-light: #f3d0bb;
    --skin-mid: #e6b197;
    --ink: #111111;
  }
  * { margin: 0; padding: 0; box-sizing: border-box; }
  html, body {
    width: 1200px; height: 705px; overflow: hidden;
    background: var(--canvas-bg);
  }
  .board {
    position: absolute; left: 360px; top: 49px;
    width: 480px; height: 607px;
    background: var(--board-white);
    overflow: hidden;
    box-shadow: 0 10px 30px rgba(0,0,0,.5);
  }
  .board-art { position: absolute; inset: 0; }
  .brand-name {
    position: absolute; left: 0; width: 310px; text-align: center;
    font-family: "Cinzel", serif; font-weight: 600; color: var(--board-white);
  }
  .brand-name--main { top: 150px; font-size: 27px; letter-spacing: 1px; }
  .brand-name--sub { top: 186px; font-size: 15px; letter-spacing: 6px; }
  .headline {
    position: absolute; left: 37px; top: 218px;
    font-family: "Open Sans", sans-serif; font-weight: 800;
    font-size: 60px; line-height: 61px; letter-spacing: -2px;
    color: var(--board-white);
    text-shadow: 2px 3px 0 var(--deep-blue);
  }
  .divider {
    position: absolute; left: 37px; top: 476px;
    width: 352px; height: 3px; background: var(--board-white);
  }
  .phone {
    position: absolute; left: 35px; top: 482px;
    font-family: "Open Sans", sans-serif; font-weight: 800;
    font-size: 44px; letter-spacing: -0.5px; color: var(--board-white);
    text-shadow: 2px 2px 0 var(--deep-blue);
  }
  .website {
    position: absolute; left: 37px; top: 532px;
    font-family: "Open Sans", sans-serif; font-weight: 700;
    font-size: 22px; letter-spacing: 0.6px; color: var(--board-white);
    text-shadow: 1px 2px 0 var(--deep-blue);
  }
  .brochure-holder {
    position: absolute; left: 392px; top: 415px;
    width: 79px; height: 152px; background: var(--board-white);
    display: flex; align-items: center; justify-content: center;
    text-align: center;
    font-family: "Bebas Neue", sans-serif; font-size: 15px; line-height: 20px;
    color: var(--ink);
  }
</style>
</head>
<body>
  <div class="board">
    <svg class="board-art" width="480" height="607" viewBox="0 0 480 607" aria-hidden="false">
      <defs>
        <linearGradient id="skin" x1="0" y1="0" x2="1" y2="1">
          <stop offset="0" stop-color="var(--skin-light)"/>
          <stop offset="1" stop-color="var(--skin-mid)"/>
        </linearGradient>
      </defs>
      <path class="blue-panel" fill="var(--brand-blue)"
            d="M10 0 H250 C380 120 440 260 452 415 V578 H14 Q0 578 0 564 V10 Q0 0 10 0 Z"/>
      <rect class="cyan-band" x="22" y="578" width="436" height="29" fill="var(--accent-cyan)"/>
      <rect class="board-handle" x="191" y="19" width="99" height="18" rx="9" fill="var(--board-white)"/>
      <path class="legs-photo" role="img" aria-label="Photo of smooth bare legs and feet standing on tiptoe"
            fill="url(#skin)" opacity="0.9"
            d="M330 0 H480 V300 L440 390 L300 420 L205 395 L262 200 Z"/>
      <circle class="brand-mark" cx="154" cy="90" r="40" fill="none" stroke="var(--board-white)" stroke-width="5"/>
    </svg>

    <div class="brand-name brand-name--main">BRIGHTSTEP</div>
    <div class="brand-name brand-name--sub">FOOT CARE</div>

    <h1 class="headline">Your<br>Fungal<br>Nail<br>Experts</h1>

    <div class="divider"></div>
    <div class="phone">(07) 312 5840</div>
    <div class="website">brightstepfootcare.co.nz</div>

    <div class="brochure-holder">BROCHURE<br>HOLDER</div>
  </div>
</body>
</html>
```